Life Coach for Lawyers Business Card Design

Elegant, original, business card design for life coaching service for associate attorneys who work in big law and struggle with stress, overwhelm, and time management. Double sided design.

Target Market(s)

Women associate attorneys who work in big law and struggle with stress, overwhelm, and time management.

Industry/Entity Type

Life Coaching

Contact Information for Business Card

Marissa Pendrell
Life Coach
518.677.3941
calmbriefcounsel.net
marissa@calmbriefcounsel.net
@calmbriefcounsel (Instagram)

Font styles to use
Other font styles liked:
• Silver South font duo. See uploaded files.

Requirements
Must have
• Icons for phone, website, email, and Instagram instead of words. Specific colors used in my logo (171B2B, 421121, FFFFFF)
Nice to have
• Foil. Embossed. Feminine design.
Should not have
• Any colors other than those used in logo. See uploaded files.

```html
<!DOCTYPE html>
<html lang="en">
<head>
<meta charset="utf-8">
<title>Calm Brief Counsel – Business Card</title>
<link rel="stylesheet" href="https://fonts.googleapis.com/css2?family=Cormorant+Garamond:wght@500&family=Cinzel:wght@400&display=swap">
<style>
  :root {
    --backdrop: #b4b3b4;
    --wine-deep: #421121;
    --wine-mid: #5b2a3a;
    --wine-soft: #6a3a4a;
    --ink-navy: #171b2b;
    --paper: #ffffff;
  }
  * { margin: 0; padding: 0; box-sizing: border-box; }
  html, body {
    width: 864px;
    height: 1200px;
    overflow: hidden;
    background: var(--backdrop);
  }
  .business-card {
    position: absolute;
    left: 112px;
    width: 640px;
    height: 366px;
    background: linear-gradient(135deg, var(--wine-soft) 0%, var(--wine-mid) 45%, var(--wine-deep) 100%);
    color: var(--paper);
    box-shadow: 0 6px 18px rgba(23, 27, 43, 0.25);
    border: 2px solid #e9e4e6;
  }
  .card-front { top: 170px; }
  .card-back { top: 654px; }

  .brand-name {
    font-family: "Cormorant Garamond", serif;
    font-weight: 500;
    text-transform: uppercase;
    letter-spacing: 0.12em;
    color: var(--paper);
    line-height: 1.1;
    text-align: center;
  }

  .front-brand {
    position: absolute;
    left: 40px;
    top: 160px;
    width: 270px;
    font-size: 30px;
  }
  .front-divider {
    position: absolute;
    left: 338px;
    top: 80px;
    width: 1px;
    height: 210px;
    background: var(--paper);
  }
  .contact-block {
    position: absolute;
    left: 364px;
    top: 92px;
    width: 260px;
    font-family: "Cinzel", serif;
  }
  .holder-name {
    font-size: 20px;
    letter-spacing: 0.04em;
    font-weight: 400;
    white-space: nowrap;
  }
  .holder-role {
    font-size: 12px;
    letter-spacing: 0.06em;
    margin-top: 10px;
  }
  .contact-list {
    list-style: none;
    margin-top: 18px;
    font-size: 10px;
    letter-spacing: 0.05em;
    text-transform: uppercase;
  }
  .contact-list li {
    display: flex;
    align-items: center;
    gap: 9px;
    margin-bottom: 10px;
    white-space: nowrap;
  }
  .contact-icon { width: 12px; height: 12px; flex: none; }

  .back-seal {
    position: absolute;
    left: 50%;
    top: 50%;
    width: 230px;
    height: 230px;
    transform: translate(-50%, -50%);
    border: 1.5px solid var(--paper);
    border-radius: 50%;
    display: flex;
    align-items: center;
    justify-content: center;
  }
  .back-brand { font-size: 26px; }
</style>
</head>
<body>

<section class="business-card card-front">
  <div class="brand-name front-brand">Calm Brief<br>Counsel</div>
  <div class="front-divider"></div>
  <div class="contact-block">
    <h1 class="holder-name">MARISSA PENDRELL</h1>
    <p class="holder-role">LIFE COACH</p>
    <ul class="contact-list">
      <li>
        <svg class="contact-icon" viewBox="0 0 12 12" fill="none" stroke="#ffffff" stroke-width="1" aria-label="Phone">
          <path d="M3 1.2 L4.6 1.2 L5.3 3.6 L4.2 4.5 Q5.2 6.8 7.5 7.8 L8.4 6.7 L10.8 7.4 L10.8 9 Q10.8 10.8 9 10.8 Q1.2 10 1.2 3 Q1.2 1.2 3 1.2 Z"/>
        </svg>
        518.677.3941
      </li>
      <li>
        <svg class="contact-icon" viewBox="0 0 12 12" fill="none" stroke="#ffffff" stroke-width="1" aria-label="Website">
          <circle cx="6" cy="6" r="5"/>
          <ellipse cx="6" cy="6" rx="2.2" ry="5"/>
          <line x1="1" y1="6" x2="11" y2="6"/>
        </svg>
        calmbriefcounsel.net
      </li>
      <li>
        <svg class="contact-icon" viewBox="0 0 12 12" fill="none" stroke="#ffffff" stroke-width="1" aria-label="Email">
          <rect x="1" y="2.5" width="10" height="7"/>
          <polyline points="1,2.5 6,6.5 11,2.5"/>
        </svg>
        marissa@calmbriefcounsel.net
      </li>
      <li>
        <svg class="contact-icon" viewBox="0 0 12 12" fill="none" stroke="#ffffff" stroke-width="1" aria-label="Social handle">
          <rect x="1.5" y="1.5" width="9" height="9"/>
        </svg>
        @calmbriefcounsel
      </li>
    </ul>
  </div>
</section>

<section class="business-card card-back">
  <div class="back-seal">
    <div class="brand-name back-brand">Calm Brief<br>Counsel</div>
  </div>
</section>

</body>
</html>
```